Classy, Elegant, Simple Business Card Design

Looking to have a classy, simple, and elegant design. Want a top notch designed business card. I really like the look of the new brivo credit card. I also like the design I attached. I am trying to reach 21-29 year old females for booking us for there wedding or event. We offer Disc Jockey Service, Photo Booth Rentals, and Uplighting .

Target Market(s)

21-28 year old females

Contact Information for Business Card

Has to have logo, website, email, and phone number

Font styles to use
Other font styles liked:
• open to font choice, modern, clean
Designer to choose
33a6d7
0791cd
0555a3
ffffff

Requirements
Must have
• Has to have logo, website, email, and phone number
Nice to have
• I really like the design of the new brivo credit card. I also included my logo and some designs I like
Should not have
• clutter or too much info

```html
<!DOCTYPE html>
<html lang="en">
<head>
<meta charset="utf-8">
<title>Tidewell Event Group – Business Card</title>
<link rel="stylesheet" href="https://fonts.googleapis.com/css2?family=Montserrat:wght@400;500;600&display=swap">
<style>
  :root {
    --backdrop: #e6e8ea;
    --card: #f6f6f4;
    --card-edge: #e2e1dc;
    --navy: #0555a3;
    --blue: #0791cd;
    --sky: #33a6d7;
    --ink-soft: #2f4a6b;
    --emboss: #e9e9e6;
    --emboss-shade: #d9d9d5;
  }
  * { margin: 0; padding: 0; box-sizing: border-box; }
  html, body {
    width: 1200px; height: 792px; overflow: hidden;
    background: var(--backdrop);
    font-family: "Montserrat", Arial, sans-serif;
  }
  .stage {
    width: 1200px; height: 792px;
    display: flex; align-items: center; justify-content: center; gap: 48px;
  }
  .card {
    position: relative;
    width: 525px; height: 300px;
    background: var(--card);
    border: 1px solid var(--card-edge);
  }
  /* front side */
  .contact {
    position: absolute; left: 44px; top: 62px; width: 230px;
    color: var(--navy);
  }
  .contact__name {
    font-size: 21px; font-weight: 500; letter-spacing: 1px; text-transform: uppercase;
    white-space: nowrap;
  }
  .contact__name strong { color: var(--blue); font-weight: 600; }
  .contact__role { font-size: 13px; margin-top: 2px; color: var(--ink-soft); }
  .contact__rule {
    width: 30px; height: 2px; background: var(--navy); margin: 12px 0 14px;
  }
  .contact__list { list-style: none; font-size: 13px; line-height: 1.45; }
  .contact__list li { display: flex; align-items: center; gap: 8px; white-space: nowrap; }
  .contact__list .address { padding-left: 20px; margin-bottom: 2px; }
  .contact__list svg { width: 12px; height: 12px; fill: var(--blue); flex: none; }
  .brand {
    position: absolute; right: 40px; top: 122px;
    display: flex; align-items: center; gap: 10px;
    font-size: 18px; font-weight: 600; letter-spacing: 1.5px; text-transform: uppercase;
    line-height: 1.25; text-align: right;
    color: var(--blue);
  }
  .brand__dot { width: 14px; height: 14px; border-radius: 50%; background: var(--blue); flex: none; }
  /* back side */
  .brand--emboss {
    top: auto; right: 44px; bottom: 48px;
    color: var(--emboss);
    text-shadow: 1px 1px 0 var(--emboss-shade);
    font-size: 22px;
  }
</style>
</head>
<body>
<main class="stage">
  <section class="card card--front" aria-label="Card front">
    <div class="contact">
      <h1 class="contact__name">Jamie <strong>Harlow</strong></h1>
      <p class="contact__role">Manager</p>
      <div class="contact__rule"></div>
      <ul class="contact__list">
        <li class="address">218 Linden Row, Easton<br>MD, ZIP 21601</li>
        <li><svg viewBox="0 0 24 24"><path d="M6.6 10.8a15.1 15.1 0 0 0 6.6 6.6l2.2-2.2a1 1 0 0 1 1-.25 11.4 11.4 0 0 0 3.6.57 1 1 0 0 1 1 1V20a1 1 0 0 1-1 1A17 17 0 0 1 3 4a1 1 0 0 1 1-1h3.5a1 1 0 0 1 1 1c0 1.25.2 2.45.57 3.570a1 1 0 0 1-.25 1z"/></svg>410-555-0182</li>
        <li><svg viewBox="0 0 24 24"><path d="M2 5h20v14H2zm2 2v.5l8 5 8-5V7l-8 5z"/></svg>hello@tidewellevents.com</li>
        <li><svg viewBox="0 0 24 24"><path d="M12 2a10 10 0 1 0 0 20 10 10 0 0 0 0-20zm0 2c.9 0 2.2 1.8 2.8 5H9.2C9.8 5.8 11.1 4 12 4zM4.3 11h4.7a20 20 0 0 0 0 2H4.3a8 8 0 0 1 0-2zm10.7 0h4.7a8 8 0 0 1 0 2H15a20 20 0 0 0 0-2zm-5.8 4h5.6c-.6 3.2-1.9 5-2.8 5s-2.2-1.8-2.8-5z"/></svg>www.tidewellevents.com</li>
      </ul>
    </div>
    <div class="brand">
      <span class="brand__dot"></span>
      <span class="brand__name">Tidewell<br>Event Group</span>
    </div>
  </section>
  <section class="card card--back" aria-label="Card back">
    <div class="brand brand--emboss">
      <span class="brand__name">Tidewell</span>
    </div>
  </section>
</main>
</body>
</html>
```